Valbrook Data Works

Our company is about IT hardwares and IT solutions. IT hardware such as PC, RAMS, storage and servers. IT solutions such as project management, BA. We are also selling new technology too.

Target Market(s)

Consumer, Small to Medium Business, Corporate

Requirements
Must have
• The business card must have the following:
• Name:
• Title:
• Contact Number:
• Email address:
• Website:
• Color: Must match the logo color upgrade

```html
<!DOCTYPE html>
<html lang="en">
<head>
<meta charset="utf-8">
<title>Valbrook Data Works — Business Card</title>
<link href="https://fonts.googleapis.com/css2?family=Lato:wght@300;400;700;900&display=swap" rel="stylesheet">
<style>
  :root{
    --backdrop:#1f1f1f;
    --card-dark:#141414;
    --card-light:#ffffff;
    --accent:#e08f2a;
    --edge-grey:#4a4a4a;
    --ink:#2b2b2b;
    --ink-soft:#3a3a3a;
    --on-dark:#ffffff;
  }
  *{box-sizing:border-box;margin:0;padding:0}
  html,body{width:1200px;height:900px;overflow:hidden}
  body{background:var(--backdrop);font-family:"Lato",sans-serif;position:relative}

  .card{position:absolute;width:560px;height:320px;border-radius:16px;overflow:hidden}
  .card--front{left:100px;top:90px;background:var(--card-dark)}
  .card--back{left:540px;top:490px;background:var(--card-light)}

  .card__edge{position:absolute;left:0;bottom:0;width:100%;height:40px}

  .brand{position:absolute;display:flex;align-items:center;gap:14px;
    font-weight:900;text-transform:uppercase;letter-spacing:1px}
  .brand__mark{width:18px;height:18px;background:var(--accent);flex:none}
  .brand__name{display:block;line-height:1.1}
  .card--front .brand{left:50%;top:108px;transform:translateX(-50%);
    font-size:36px;color:var(--on-dark)}
  .card--back .brand{left:40px;top:118px;width:210px;font-size:24px;color:var(--ink)}
  .card--back .brand__mark{width:14px;height:14px}

  .divider{position:absolute;left:268px;top:70px;width:2px;height:160px;background:var(--ink)}

  .contact{position:absolute;left:292px;top:78px;color:var(--ink-soft)}
  .contact__name{font-size:21px;color:var(--accent);font-weight:300;text-transform:uppercase;letter-spacing:.3px}
  .contact__name b{font-weight:700}
  .contact__title{font-size:14px;margin-top:4px;margin-bottom:22px}
  .contact__line{display:flex;align-items:center;gap:10px;font-size:14px;margin-bottom:9px}
  .contact__line svg{width:16px;height:16px;flex:none;fill:var(--accent)}
  .contact__web{font-size:15px;font-weight:700;color:var(--accent);margin-top:10px}
</style>
</head>
<body>

<section class="card card--front" aria-label="Card front">
  <div class="brand"><span class="brand__mark"></span><span class="brand__name">Valbrook<br>Data Works</span></div>
  <svg class="card__edge" viewBox="0 0 560 40" preserveAspectRatio="none">
    <path d="M0 30 L330 30 L330 40 L0 40 Z" fill="var(--edge-grey)"/>
    <path d="M330 40 C330 26 338 22 352 22 L560 22 L560 40 Z" fill="var(--accent)"/>
  </svg>
</section>

<section class="card card--back" aria-label="Card back">
  <div class="brand"><span class="brand__mark"></span><span class="brand__name">Valbrook<br>Data Works</span></div>
  <div class="divider"></div>
  <div class="contact">
    <p class="contact__name">Maren <b>Holloway</b></p>
    <p class="contact__title">Managing Director</p>
    <p class="contact__line">
      <svg viewBox="0 0 16 16"><path d="M3 2h3l1.5 3.5-2 1.2a8 8 0 0 0 3.8 3.8l1.2-2L14 10v3a1 1 0 0 1-1 1A11 11 0 0 1 2 3a1 1 0 0 1 1-1z"/></svg>
      <span>01632 960418</span>
    </p>
    <p class="contact__line">
      <svg viewBox="0 0 16 16"><path d="M1 3h14v10H1z M1.5 3.5 8 9l6.5-5.5" stroke="#fff" stroke-width="1.2"/></svg>
      <span>hello@valbrookdata.co.uk</span>
    </p>
    <p class="contact__web">www.valbrookdata.co.uk</p>
  </div>
  <svg class="card__edge" viewBox="0 0 560 40" preserveAspectRatio="none">
    <path d="M0 30 L400 30 L400 40 L0 40 Z" fill="var(--edge-grey)"/>
    <path d="M400 40 C400 26 408 22 422 22 L560 22 L560 40 Z" fill="var(--accent)"/>
  </svg>
</section>

</body>
</html>
```